Visitenkarten
Zielgruppe
Hallo!
Für mein Unternehmen habe ich bereits einmal ein Logo mit Feldmotte erstellen lassen (leider weiß ich den Designer nicht mehr).
Unter meinem Unternehmen Vollmerhaus Coaching laufen zwei Unternehmensbereiche, für die ich jetzt Visitenkarten benötige. Daher ist der Stil der beiden Teilbereiche ähnlich. Die Logos existieren schon. Nun benötige ich für beide Bereiche Visitenkarten. Für beide Bereiche benötige ich im Anschluss im 1:1 Auftrage noch Dateien, damit die ich Logos auch gut auf Webseiten und Social Medien nutzen kann.
Vollmerhaus HR Services <: bietet HR Dienstleistungen rund um das Personalwesen an: HR-Trainings, HR Outsourcing und Projekt- und Interimsmanagement
Sattelklar Balance | Vollmerhaus Coaching: bietet Mental- und Hypnosecoachings an, Trainings zur mentalen Fitness, Stress- und Blockadenlösung im Reitsport und optimale Turniervorbereitung
Aufgabenstellung
Bitte den bestehenden Brandguide und die Materialien nutzen. Eigene Ideen sind willkommen, sollen aber in der Logik bleiben.
Daten Visitenkarte Vollmerhaus HR Services:
Annelie Vollmerhaus
Dipl. Sozialwirt, Business Coach, Mentaltrainer
Telefon +49 (0)1593 26 48 357
Mobil +49 (0)171 58 93 704
Mail: annelie@vollmerhaus-beratung.example
Vollmerhaus HR Services | Vollmerhaus Coaching
Am Lindenhang 9b
29643 Neuenkirchen
Daten Visitenkarte Vollmerhaus Sattelklar Balance:
Dipl. Sozialwirt, Hypnosecoach, Mentaltrainer
Sattelklar Balance | Vollmerhaus Coaching

```html
<!DOCTYPE html>
<html lang="de">
<head>
<meta charset="utf-8">
<title>Visitenkarten Vollmerhaus Coaching</title>
<link href="https://fonts.googleapis.com/css2?family=Arimo:wght@400;700&family=Poppins:wght@500&display=swap" rel="stylesheet">
<style>
:root{
  --bg:#e9e8ec;
  --card:#ffffff;
  --ink:#3f3566;
  --purple:#6a5a9c;
  --purple-dark:#4a3f78;
  --lavender:#d9d5e6;
  --grey:#e6e5ea;
  --horse:#cfc8e4;
}
*{box-sizing:border-box;margin:0;padding:0}
html,body{width:960px;height:1200px;overflow:hidden;background:var(--bg)}
body{font-family:"Arimo",Arial,sans-serif;color:var(--ink)}
.sheet{position:relative;width:960px;height:1200px;display:grid;grid-template-columns:420px 420px;grid-template-rows:260px 260px;gap:80px 40px;justify-content:center;align-content:center}
.card{position:relative;width:420px;height:260px;background:var(--card);box-shadow:0 6px 18px rgba(40,30,70,.18);overflow:hidden}
.card svg.bands{position:absolute;inset:0;width:100%;height:100%}
.brand{position:absolute;font-family:"Poppins",Arial,sans-serif;font-weight:500;color:var(--ink);letter-spacing:1px;text-transform:uppercase;line-height:1.25}
.card--back .brand{left:30px;top:92px;font-size:20px;white-space:nowrap}
.divider{position:absolute;left:196px;top:38px;width:1.5px;height:168px;background:var(--ink)}
.card--front .brand{left:14px;top:104px;width:170px;font-size:14px;text-align:center}
.details{position:absolute;left:210px;top:38px;width:200px}
.name{font-weight:700;font-size:14.5px;letter-spacing:.3px;text-transform:uppercase}
.role{font-size:7.5px;letter-spacing:.6px;text-transform:uppercase;margin-top:3px;padding-bottom:4px;border-bottom:1px solid var(--ink)}
.contacts{list-style:none;margin-top:14px;font-size:8px;letter-spacing:.4px}
.contacts li{display:flex;align-items:flex-start;gap:8px;margin-bottom:7px;line-height:1.3}
.contacts svg{flex:none;width:10px;height:10px;fill:var(--ink)}
.horse{position:absolute;left:24px;top:54px;width:90px;height:110px;border-radius:40% 50% 30% 40%;background:radial-gradient(circle at 50% 45%,var(--horse),rgba(207,200,228,.15))}
.card--riding-back .brand{left:130px;top:96px;width:170px;font-size:12px;text-align:center;white-space:normal}
.card--riding-front .horse{left:14px;top:62px;width:70px;height:86px}
.card--riding-front .brand{left:90px;top:92px;width:98px;font-size:8px;letter-spacing:.5px}
</style>
</head>
<body>
<main class="sheet">

  <section class="card card--back">
    <svg class="bands" viewBox="0 0 420 260" aria-hidden="true">
      <polygon points="220,0 300,0 420,120 420,175" fill="var(--grey)"/>
      <polygon points="270,0 330,0 420,90 420,150" fill="var(--purple-dark)"/>
      <polygon points="345,0 365,0 420,55 420,75" fill="var(--purple)"/>
      <polygon points="0,222 300,222 420,205 420,215 300,232 0,232" fill="var(--lavender)"/>
      <polygon points="0,232 300,232 420,215 420,260 0,260" fill="var(--purple)"/>
    </svg>
    <p class="brand">Vollmerhaus Coaching</p>
  </section>

  <section class="card card--front">
    <svg class="bands" viewBox="0 0 420 260" aria-hidden="true">
      <polygon points="0,220 320,220 420,160 420,170 325,230 0,230" fill="var(--lavender)"/>
      <polygon points="0,232 330,232 420,178 420,260 0,260" fill="var(--purple)"/>
    </svg>
    <p class="brand">Vollmerhaus Coaching</p>
    <div class="divider"></div>
    <div class="details">
      <p class="name">Annelie Vollmerhaus</p>
      <p class="role">Dipl. Social Economist, Business Coach, Mental Trainer</p>
      <ul class="contacts">
        <li><svg viewBox="0 0 10 10"><path d="M2 0.5l2 2-1 1.2c.6 1.3 1.6 2.3 2.9 2.9l1.2-1 2 2-1.3 1.9C4 9.2.8 6 .2 1.8z"/></svg>+49 (0)1593 26 48 357</li>
        <li><svg viewBox="0 0 10 10"><path d="M2.5 0h5v10h-5zM3.3 1v7h3.4V1z"/></svg>+49 (0)171 58 93 704</li>
        <li><svg viewBox="0 0 10 10"><path d="M0 2h10v6H0zM.8 2.6L5 5.6l4.2-3z" fill-rule="evenodd"/></svg>annelie@vollmerhaus-beratung.example</li>
        <li><svg viewBox="0 0 10 10"><path d="M5 0a3.4 3.4 0 013.4 3.4C8.4 6 5 10 5 10S1.6 6 1.6 3.4A3.4 3.4 0 015 0zm0 2a1.4 1.4 0 100 2.8A1.4 1.4 0 005 2z"/></svg><span>Vollmerhaus HR Services |<br>Vollmerhaus Coaching<br>Am Lindenhang 9b 29643 Neuenkirchen</span></li>
      </ul>
    </div>
  </section>

  <section class="card card--back card--riding-back">
    <svg class="bands" viewBox="0 0 420 260" aria-hidden="true">
      <polygon points="230,0 290,0 420,130 330,200 0,200 0,195 320,195" fill="var(--grey)"/>
      <polygon points="280,0 340,0 420,80 420,165" fill="var(--purple-dark)"/>
      <polygon points="355,0 375,0 420,45 420,65" fill="var(--purple)"/>
      <polygon points="0,215 330,215 420,170 420,180 335,225 0,225" fill="var(--lavender)"/>
      <polygon points="0,228 340,228 420,188 420,260 0,260" fill="var(--purple)"/>
    </svg>
    <div class="horse" role="img" aria-label="Zeichnung eines galoppierenden Pferdes in Lila"></div>
    <p class="brand">Vollmerhaus Sattelklar Balance</p>
  </section>

  <section class="card card--front card--riding-front">
    <svg class="bands" viewBox="0 0 420 260" aria-hidden="true">
      <polygon points="0,220 320,220 420,160 420,170 325,230 0,230" fill="var(--lavender)"/>
      <polygon points="0,232 330,232 420,178 420,260 0,260" fill="var(--purple)"/>
    </svg>
    <div class="horse" role="img" aria-label="Zeichnung eines galoppierenden Pferdes in Lila"></div>
    <p class="brand">Vollmerhaus Sattelklar Balance</p>
    <div class="divider"></div>
    <div class="details">
      <p class="name">Annelie Vollmerhaus</p>
      <p class="role">Dipl. Social Economist, Hypnosis Coach, Mental Trainer</p>
      <ul class="contacts">
        <li><svg viewBox="0 0 10 10"><path d="M2 0.5l2 2-1 1.2c.6 1.3 1.6 2.3 2.9 2.9l1.2-1 2 2-1.3 1.9C4 9.2.8 6 .2 1.8z"/></svg>+49 (0)1593 26 48 357</li>
        <li><svg viewBox="0 0 10 10"><path d="M2.5 0h5v10h-5zM3.3 1v7h3.4V1z"/></svg>+49 (0)171 58 93 704</li>
        <li><svg viewBox="0 0 10 10"><path d="M0 2h10v6H0zM.8 2.6L5 5.6l4.2-3z" fill-rule="evenodd"/></svg>annelie@vollmerhaus-beratung.example</li>
        <li><svg viewBox="0 0 10 10"><path d="M5 0a3.4 3.4 0 013.4 3.4C8.4 6 5 10 5 10S1.6 6 1.6 3.4A3.4 3.4 0 015 0zm0 2a1.4 1.4 0 100 2.8A1.4 1.4 0 005 2z"/></svg><span>Sattelklar Balance | Vollmerhaus Coaching<br>Am Lindenhang 9b<br>29643 Neuenkirchen</span></li>
      </ul>
    </div>
  </section>

</main>
</body>
</html>
```